Bref créative
Business Card, Stationary, etc. for a plastic surgeon's office
Brennholt Clinic (Plastic & Reconstructive Surgery)
Use standard fonts
Play with the fonts to see what looks best.
Professional
Gregory T. Brennholt, DO
Plastic Surgeon
475 Corwin Haley Blvd, Ste. 260
Sandmere Cove, FL 32190
(Tollmead Business Park)
555-GET-TRIM (555-438-8746)
555-438-FAX5 (555-438-3295)
drbrennholt@brennholtclinic.example
www.brennholtclinic.example
This card, stationary, etc. should look clean and professional with my existing logo purchased from a designer using this sight.
I would like the back of the business card to contain the logo (i.e. Brennholt Clinic in larger letters with logo between the two words with Plastic & Reconstructive Surgery written below the main title with smaller font). Thanks and good luck!!!
logo vector file

```html
<!DOCTYPE html>
<html lang="en">
<head>
<meta charset="utf-8">
<title>Brennholt Clinic — Stationery Set</title>
<link href="https://fonts.googleapis.com/css2?family=Cormorant+Garamond:wght@500;600&family=Montserrat:wght@400;500;600&family=Open+Sans:wght@400&display=swap" rel="stylesheet">
<style>
  :root{
    --backdrop:#9c8150;
    --paper:#ffffff;
    --paper-shade:#f1efec;
    --gold:#c9a65a;
    --gold-light:#e0c68c;
    --gold-deep:#a9853d;
    --ink:#3a3a3a;
    --ink-soft:#7a7a7a;
    --black:#111111;
  }
  *{box-sizing:border-box;margin:0;padding:0}
  html,body{width:1200px;height:862px;overflow:hidden}
  body{background:var(--backdrop);position:relative;font-family:"Open Sans",Arial,sans-serif;color:var(--ink)}

  .piece{position:absolute;background:var(--paper);box-shadow:0 4px 14px rgba(0,0,0,.25);overflow:hidden}

  .brand{text-align:center;color:var(--gold)}
  .brand-name{font-family:"Cormorant Garamond",Georgia,serif;font-weight:600;color:var(--gold);line-height:1;display:block}
  .brand-tag{font-family:"Montserrat",Arial,sans-serif;font-weight:500;letter-spacing:.14em;text-transform:uppercase;color:var(--gold);display:block;margin-top:4px}

  /* letterhead */
  .letterhead{left:40px;top:40px;width:360px;height:466px}
  .letterhead .brand{margin-top:22px}
  .letterhead .brand-name{font-size:30px}
  .letterhead .brand-tag{font-size:6px}
  .letter-body{padding:26px 34px 0;font-size:8.5px;line-height:1.65;color:var(--ink)}
  .letter-body .greeting{font-size:13px;margin-bottom:10px}
  .letter-body p{margin-bottom:10px}
  .letterhead .foot{position:absolute;left:0;bottom:0;width:100%;height:70px}
  .foot-text{position:absolute;left:0;bottom:12px;width:100%;text-align:center;font-family:"Montserrat",Arial,sans-serif;font-size:6px;color:#fff;letter-spacing:.02em;white-space:nowrap}

  /* fax sheet */
  .fax{left:420px;top:40px;width:360px;height:466px}
  .fax-title{font-family:"Montserrat",Arial,sans-serif;font-size:22px;font-weight:500;color:var(--ink-soft);letter-spacing:.06em;margin:28px 0 0 30px}
  .fax .brand{position:absolute;right:26px;top:22px;text-align:right}
  .fax .brand-name{font-size:20px}
  .fax .brand-tag{font-size:5px}
  .fax-lines{position:absolute;left:30px;right:30px;top:110px}
  .fax-lines span{display:block;height:26px;border-bottom:1px solid var(--paper-shade)}
  .fax .foot{position:absolute;left:0;bottom:0;width:100%;height:70px}

  /* cards */
  .card{width:360px;height:206px;border-radius:10px;left:800px}
  .card-front{top:40px}
  .card-front .brand{margin-top:30px}
  .card-front .brand-name{font-size:34px}
  .card-front .brand-tag{font-size:6.5px}
  .name-band{position:absolute;left:0;top:110px;width:100%;height:24px;background:var(--gold);display:flex;align-items:center;justify-content:flex-end;padding-right:22px;font-family:"Montserrat",Arial,sans-serif;font-size:9px;color:#fff;gap:8px}
  .name-band strong{font-weight:600}
  .card-details{position:absolute;top:146px;left:22px;right:22px;display:flex;justify-content:space-between;font-size:7px;line-height:1.7;color:var(--ink-soft)}
  .card-details address{font-style:normal}
  .contact-list{list-style:none}
  .contact-list li{display:flex;align-items:center;gap:5px;white-space:nowrap}
  .contact-list svg{width:8px;height:8px;fill:var(--gold)}

  .card-back{top:266px;background:var(--black)}
  .card-back .brand{margin-top:62px}
  .card-back .brand-name{font-size:36px}
  .card-back .brand-tag{font-size:6.5px}
  .card-url{position:absolute;left:24px;bottom:18px;font-family:"Montserrat",Arial,sans-serif;font-size:8px;color:var(--gold)}

  .card-gold{top:492px;background:linear-gradient(135deg,var(--gold-light),var(--gold))}
  .card-gold .brand{margin-top:62px}
  .card-gold .brand-name,.card-gold .brand-tag{color:#fff}
  .card-gold .brand-name{font-size:36px}
  .card-gold .brand-tag{font-size:6.5px}
  .card-gold .card-url{color:#fff}

  /* envelope */
  .envelope{left:40px;top:530px;width:740px;height:300px;background:var(--paper)}
  .envelope .brand{position:absolute;left:34px;top:30px;text-align:left}
  .envelope .brand-name{font-size:26px}
  .envelope .brand-tag{font-size:5.5px}
  .return-address{position:absolute;left:34px;top:86px;font-size:7.5px;line-height:1.6;color:var(--ink-soft);font-style:normal}
  .envelope .wave{position:absolute;left:0;bottom:0;width:100%;height:110px}
  .envelope .card-url{left:auto;right:34px;bottom:16px;color:#fff;font-size:10px}
</style>
</head>
<body>

<section class="piece letterhead">
  <div class="brand">
    <span class="brand-name">Brennholt Clinic</span>
    <span class="brand-tag">Plastic &amp; Reconstructive Surgery</span>
  </div>
  <div class="letter-body">
    <p class="greeting">Hello,</p>
    <p>Thank you for choosing our clinic for your care. We value the trust you place in our team and look forward to guiding you through every step of your consultation, procedure and recovery with attention and respect.</p>
    <p>Please review the enclosed details before your next visit and call our office with any questions you may have.</p>
  </div>
  <svg class="foot" viewBox="0 0 360 70" preserveAspectRatio="none" aria-hidden="true">
    <path d="M0 30 Q180 0 360 22 L360 70 L0 70 Z" fill="var(--gold-light)"/>
    <path d="M0 42 Q180 14 360 34 L360 70 L0 70 Z" fill="var(--gold)"/>
  </svg>
  <p class="foot-text">475 Corwin Haley Blvd, Ste. 260 · Sandmere Cove, FL 32190 · 555-438-8746 · www.brennholtclinic.example</p>
</section>

<section class="piece fax">
  <h2 class="fax-title">Fax Sheet</h2>
  <div class="brand">
    <span class="brand-name">Brennholt Clinic</span>
    <span class="brand-tag">Plastic &amp; Reconstructive Surgery</span>
  </div>
  <div class="fax-lines"><span></span><span></span><span></span><span></span><span></span><span></span><span></span><span></span><span></span><span></span></div>
  <svg class="foot" viewBox="0 0 360 70" preserveAspectRatio="none" aria-hidden="true">
    <path d="M0 30 Q180 0 360 22 L360 70 L0 70 Z" fill="var(--gold-light)"/>
    <path d="M0 42 Q180 14 360 34 L360 70 L0 70 Z" fill="var(--gold)"/>
  </svg>
</section>

<section class="piece card card-front">
  <div class="brand">
    <span class="brand-name">Brennholt Clinic</span>
    <span class="brand-tag">Plastic &amp; Reconstructive Surgery</span>
  </div>
  <div class="name-band"><strong>Gregory T. Brennholt, DO</strong><span>|</span><span>Plastic Surgeon</span></div>
  <div class="card-details">
    <address>475 Corwin Haley Blvd, Ste. 260<br>Sandmere Cove, FL 32190<br>Tollmead Business Park</address>
    <ul class="contact-list">
      <li><svg viewBox="0 0 10 10"><path d="M2 0h2l1 3-1.3 1a6 6 0 0 0 2.3 2.3L7 5l3 1v2a2 2 0 0 1-2 2A8 8 0 0 1 0 2a2 2 0 0 1 2-2z"/></svg>555-GET-TRIM (555-438-8746)</li>
      <li><svg viewBox="0 0 10 10"><rect x="1" y="3" width="8" height="6"/><rect x="3" y="0" width="4" height="3"/></svg>555-438-FAX5 (555-438-3295)</li>
      <li><svg viewBox="0 0 10 10"><path d="M0 2h10v6H0z M0 2l5 3.5L10 2"/></svg>drbrennholt@brennholtclinic.example</li>
    </ul>
  </div>
</section>

<section class="piece card card-back">
  <div class="brand">
    <span class="brand-name">Brennholt Clinic</span>
    <span class="brand-tag">Plastic &amp; Reconstructive Surgery</span>
  </div>
  <p class="card-url">www.brennholtclinic.example</p>
</section>

<section class="piece card card-gold">
  <div class="brand">
    <span class="brand-name">Brennholt Clinic</span>
    <span class="brand-tag">Plastic &amp; Reconstructive Surgery</span>
  </div>
  <p class="card-url">www.brennholtclinic.example</p>
</section>

<section class="piece envelope">
  <div class="brand">
    <span class="brand-name">Brennholt Clinic</span>
    <span class="brand-tag">Plastic &amp; Reconstructive Surgery</span>
  </div>
  <address class="return-address">475 Corwin Haley Blvd, Ste. 260<br>Sandmere Cove, FL 32190<br>Tollmead Business Park</address>
  <svg class="wave" viewBox="0 0 740 110" preserveAspectRatio="none" aria-hidden="true">
    <path d="M0 60 Q370 10 740 40 L740 110 L0 110 Z" fill="var(--gold-light)"/>
    <path d="M0 78 Q370 30 740 60 L740 110 L0 110 Z" fill="var(--gold)"/>
  </svg>
  <p class="card-url">www.brennholtclinic.example</p>
</section>

</body>
</html>
```